Educational Agency in Abu Dhabi looking for an 8 pages website

We are looking for an 8 pages design for a website, we already have one but we need to refine it and it is www.brightcampuslink.ae - Please base it on logo colours (attached) I have uploaded our logo, website content logo colors to use it for the scheme.
We are looking for a smooth look and content added if possible, I also attached content and logo

Industry/Entity Type

Education

Coding

Coded - Design and coding required

Number of Pages Required

5+ page

```html
<!DOCTYPE html>
<html lang="en">
<head>
<meta charset="utf-8">
<title>Bright Campus — Study Abroad Consultancy</title>
<link href="https://fonts.googleapis.com/css2?family=Raleway:wght@400;500;600;700;800&display=swap" rel="stylesheet">
<style>
:root{
  --navy:#1f3466;
  --navy-deep:#182a55;
  --ink:#2b2b2b;
  --muted:#555;
  --grey-bg:#ececec;
  --line:#c9ccd6;
  --white:#fff;
  --black:#0d0d0d;
  --footer-grey:#4a4a4a;
}
*{box-sizing:border-box;margin:0;padding:0}
html,body{width:1200px;height:3947px;overflow:hidden}
body{font-family:"Raleway",Arial,sans-serif;color:var(--ink);background:var(--white);position:relative}
.abs{position:absolute}

/* header */
.topbar{position:absolute;left:0;top:0;width:1200px;height:82px;background:var(--white)}
.apply-tab{position:absolute;right:0;top:0;width:270px;height:26px;background:var(--navy-deep);color:#fff;font-size:13px;font-weight:700;letter-spacing:.5px;text-align:center;line-height:26px}
.contact-item{position:absolute;top:46px;font-size:15px;color:var(--ink);display:flex;align-items:center;gap:8px}
.contact-item svg{width:22px;height:22px}
.follow{position:absolute;top:48px;left:958px;font-size:15px;display:flex;align-items:center;gap:6px}
.follow i{display:inline-block;width:18px;height:18px;border-radius:50%;background:var(--navy)}
.brand-block{position:absolute;left:0;top:0;width:263px;height:168px;background:var(--white);display:flex;align-items:center;justify-content:center;gap:10px}
.brand-block .dot{width:22px;height:22px;border-radius:50%;background:var(--navy)}
.brand-name{font-size:30px;font-weight:800;color:var(--navy-deep);line-height:1}
.nav{position:absolute;left:263px;top:82px;width:937px;height:44px;background:var(--navy);display:flex;align-items:center;justify-content:space-around;padding:0 10px}
.nav a{color:#fff;font-size:13px;font-weight:600;text-decoration:none}

/* hero */
.hero{position:absolute;left:0;top:0;width:1200px;height:690px;background:linear-gradient(180deg,#6d6e73 0%,#8d7c6c 35%,#5b4a3f 70%,#3a3230 100%)}
.hero-photo{position:absolute;inset:126px 0 0 0}
.hero-quote{position:absolute;left:0;top:478px;width:1200px;text-align:center;color:#fff;font-size:38px;font-weight:500;line-height:46px}
.hero-cite{position:absolute;left:0;top:570px;width:1200px;text-align:center;color:#fff;font-size:16px}
.dots{position:absolute;top:634px;left:0;width:1200px;display:flex;justify-content:center;gap:10px}
.dots span{width:10px;height:10px;border-radius:50%;border:2px solid #fff}
.dots span.on{background:#fff}

/* section titles */
.sec-title{position:absolute;left:0;width:1200px;text-align:center;font-size:38px;color:var(--navy);font-weight:500;letter-spacing:1px}
.sec-title b{font-weight:800}
.sec-title::after{content:"";display:block;width:60px;height:3px;background:var(--navy);margin:8px auto 0}

/* about */
.about-text{position:absolute;left:125px;top:815px;width:950px;font-size:13px;line-height:19px;color:var(--muted)}
.pillars{position:absolute;left:125px;top:970px;width:950px;display:flex}
.pillar{flex:1;padding:0 22px;text-align:center;border-right:1px solid var(--line)}
.pillar:last-child{border-right:none;text-align:left}
.pillar h3{font-size:18px;font-weight:500;color:var(--navy);display:flex;align-items:center;justify-content:center;gap:8px;margin-bottom:14px}
.pillar h3 svg{width:26px;height:26px}
.pillar p{font-size:13px;line-height:19px;color:var(--muted)}
.pillar ul{list-style:none;font-size:13px;line-height:21px;color:var(--muted)}
.pillar li::before{content:"•";color:var(--navy);margin-right:8px}

/* destinations */
.destinations{position:absolute;left:0;top:1257px;width:1200px;height:773px;background:var(--grey-bg);overflow:hidden}
.dest-label{position:absolute;font-size:16px;color:var(--ink);text-align:center;line-height:19px}
.dest-label b{color:var(--navy);font-weight:700}

/* application */
.apply{position:absolute;left:0;top:2030px;width:1200px;height:437px;background:var(--navy-deep)}
.apply-photo{position:absolute;right:0;top:0;width:560px;height:437px;background:linear-gradient(100deg,#1d2f5e 0%,#3e5a94 45%,#7e95c4 100%)}
.apply h2{position:absolute;left:152px;top:70px;font-size:24px;font-weight:500;color:#fff}
.field{position:absolute;left:152px;width:395px;height:34px;background:#fff;font-size:13px;color:#777;padding:0 12px;line-height:34px}
.field em{color:#d22;font-style:normal}
.apply-btn{position:absolute;left:152px;top:312px;width:130px;height:36px;border:2px solid #fff;color:#fff;font-size:15px;text-align:center;line-height:32px}

/* why */
.cards{position:absolute;left:105px;top:2645px;width:990px;display:flex;gap:18px}
.card{width:234px;height:196px;background:var(--navy);color:#fff;text-align:center;padding:52px 14px 0;position:relative}
.card .icon{position:absolute;left:50%;top:-26px;width:52px;height:52px;margin-left:-26px;border-radius:50%;background:#fff;border:3px solid var(--navy);display:flex;align-items:center;justify-content:center}
.card .icon svg{width:26px;height:26px}
.card h4{font-size:14px;font-weight:700;line-height:18px;margin-bottom:12px}
.card p{font-size:11px;line-height:15px;opacity:.9}
.read-more{position:absolute;left:555px;top:2885px;width:130px;height:38px;background:var(--navy-deep);color:#fff;font-size:15px;text-align:center;line-height:38px}

/* partners */
.partners{position:absolute;left:0;top:2993px;width:1200px;height:421px;background:var(--grey-bg)}
.badge{position:absolute}

/* newsletter */
.newsletter{position:absolute;left:0;top:3414px;width:1200px;height:74px;background:var(--black)}
.newsletter .nl-icon{position:absolute;left:160px;top:19px;width:36px;height:36px;border-radius:50%;background:#d9d9d9;display:flex;align-items:center;justify-content:center}
.newsletter h5{position:absolute;left:212px;top:20px;font-size:26px;font-weight:500;color:#fff}
.newsletter .chev{position:absolute;left:448px;top:20px}
.nl-input{position:absolute;left:492px;top:24px;width:400px;height:28px;background:#fff;font-size:11px;color:#777;padding-left:10px;line-height:28px}
.nl-btn{position:absolute;left:902px;top:24px;width:134px;height:28px;background:#bdbdbd;color:#fff;font-size:12px;font-weight:700;text-align:center;line-height:28px;letter-spacing:.5px}

/* footer */
.footer{position:absolute;left:0;top:3488px;width:1200px;height:383px;background:var(--navy)}
.footer-brand{position:absolute;left:135px;top:115px;width:170px;text-align:center;color:#fff;font-size:26px;font-weight:800;line-height:30px}
.footer-social{position:absolute;left:108px;top:258px;display:flex;gap:10px}
.footer-social i{width:28px;height:28px;border-radius:50%;border:2px solid #fff;display:block}
.footer h6{position:absolute;top:50px;font-size:18px;font-weight:500;color:#fff;letter-spacing:1px}
.footer address{position:absolute;left:403px;top:90px;font-style:normal;color:#fff;font-size:15px;line-height:21px}
.gi{position:absolute;background:#fff;font-size:12px;color:#777;padding-left:8px;line-height:38px;height:38px}
.gi.desc{height:64px;line-height:22px;padding-top:6px}
.submit{position:absolute;left:697px;top:287px;width:130px;height:38px;border:2px solid #fff;color:#fff;font-size:15px;font-weight:700;text-align:center;line-height:34px;letter-spacing:.5px}
.copyright{position:absolute;left:0;top:3871px;width:1200px;height:76px;background:var(--footer-grey);color:#ddd;font-size:13px;text-align:center;line-height:76px}
</style>
</head>
<body>

<!-- hero -->
<section class="hero">
  <div class="hero-photo" role="img" aria-label="Photo of a group of smiling university students standing together outdoors"></div>
  <p class="hero-quote">There is no place in the future for<br>those who lack science &amp; knowledge</p>
  <p class="hero-cite">— Rashid Al Noor</p>
  <div class="dots"><span class="on"></span><span></span><span></span></div>
</section>

<!-- header -->
<header>
  <div class="topbar"></div>
  <div class="apply-tab">MAKE AN APPLICATION</div>
  <div class="contact-item" style="left:555px">
    <svg viewBox="0 0 24 24"><path fill="#1f3466" d="M6.6 10.8a15.1 15.1 0 0 0 6.6 6.6l2.2-2.2c.3-.3.7-.4 1-.2 1.1.4 2.3.6 3.6.6.6 0 1 .4 1 1V20c0 .6-.4 1-1 1A17 17 0 0 1 3 4c0-.6.4-1 1-1h3.5c.6 0 1 .4 1 1 0 1.3.2 2.5.6 3.6.1.3 0 .7-.2 1z"/></svg>
    1-800-555-0142
  </div>
  <div class="contact-item" style="left:728px">
    <svg viewBox="0 0 24 24"><rect x="2" y="5" width="20" height="14" rx="2" fill="#1f3466"/><path d="M3 6l9 7 9-7" stroke="#fff" stroke-width="1.6" fill="none"/></svg>
    info@brightcampuslink.ae
  </div>
  <div class="follow">Follow us <i></i><i></i><i></i><i></i><i></i></div>
  <nav class="nav">
    <a>About Us</a><a>Why Study Abroad</a><a>Study Destinations</a><a>Our Services</a><a>Study English Language</a><a>Courses</a><a>Scholarships</a><a>Apply Now</a><a>Contact Us</a>
  </nav>
  <div class="brand-block"><span class="dot"></span><span class="brand-name">BRIGHT<br>CAMPUS</span></div>
</header>

<!-- about -->
<h2 class="sec-title" style="top:735px"><b>ABOUT US</b></h2>
<p class="about-text">BRIGHT CAMPUS is the fastest growing educational and study abroad consultancy firm in the UAE. It is officially recognized by the National Board of Higher Learning, Global Learning Council, Intl Agent Network and QualityMark. Established in 2015, BRIGHT CAMPUS provides professional consulting services to facilitate aspiring students in finding a suitable overseas educational institution in the USA, UK, Australia, Malaysia, Europe, Middle East, South Africa and more. We take pride in our holistic and bespoke program that ensures every student makes the right career choice and finds the right course to lead them there, all subject to their existing qualifications, interests, needs, and their government's vision. We also act as study abroad consultants for various government sectors and corporations.</p>

<div class="pillars">
  <div class="pillar">
    <h3><svg viewBox="0 0 24 24"><circle cx="12" cy="12" r="11" fill="none" stroke="#1f3466" stroke-width="1.6"/><ellipse cx="12" cy="12" rx="6" ry="3.5" fill="none" stroke="#1f3466" stroke-width="1.6"/><circle cx="12" cy="12" r="1.6" fill="#1f3466"/></svg>Our vision</h3>
    <p>To become the region's leading educational consultant by providing customized, sector leading market knowledge and expert advice to students and educational institutions abroad.</p>
  </div>
  <div class="pillar">
    <h3><svg viewBox="0 0 24 24"><circle cx="12" cy="12" r="11" fill="none" stroke="#1f3466" stroke-width="1.6"/><circle cx="12" cy="12" r="6" fill="none" stroke="#1f3466" stroke-width="1.6"/><circle cx="12" cy="12" r="2" fill="#1f3466"/></svg>Our Mission</h3>
    <p>To fully prepare students from all corners of the world with the necessary tools and pre-requisites for overseas studies, through an integrated system of facilities, expert consultancy services and a guide to accessing our strategic network of the world's highest-ranking universities.</p>
  </div>
  <div class="pillar">
    <h3><svg viewBox="0 0 24 24"><circle cx="12" cy="12" r="11" fill="none" stroke="#1f3466" stroke-width="1.6"/><path d="M7 12.5l3.2 3.2L17 9" stroke="#1f3466" stroke-width="2" fill="none"/></svg>Our Values</h3>
    <ul>
      <li>Credibility</li>
      <li>Social Responsibility</li>
      <li>Excellence in service delivery</li>
      <li>Strengthening Partnerships</li>
      <li>Implementing best practices in the educational consultancy</li>
    </ul>
  </div>
</div>

<!-- destinations -->
<section class="destinations">
  <h2 class="sec-title" style="top:62px">STUDY <b>DESTINATIONS</b></h2>
  <svg class="abs" style="left:0;top:0" width="1200" height="773" viewBox="0 0 1200 773">
    <circle cx="600" cy="760" r="420" fill="#e2e2e2"/>
    <circle cx="600" cy="760" r="420" fill="none" stroke="#1f3466" stroke-width="3"/>
    <circle cx="600" cy="760" r="330" fill="#d9d9d9"/>
    <circle cx="600" cy="760" r="270" fill="#e6e6e6"/>
    <g stroke="#1f3466" stroke-width="2" stroke-dasharray="3 5">
      <line x1="250" y1="671" x2="185" y2="671"/>
      <line x1="255" y1="484" x2="310" y2="510"/>
      <line x1="389" y1="329" x2="420" y2="390"/>
      <line x1="600" y1="247" x2="600" y2="340"/>
      <line x1="810" y1="311" x2="785" y2="385"/>
      <line x1="923" y1="489" x2="885" y2="510"/>
      <line x1="936" y1="671" x2="1010" y2="671"/>
    </g>
    <g fill="#1f3466">
      <circle cx="380" cy="563" r="7"/><circle cx="445" cy="470" r="7"/><circle cx="600" cy="430" r="7"/>
      <circle cx="755" cy="470" r="7"/><circle cx="820" cy="563" r="7"/><circle cx="330" cy="680" r="7"/><circle cx="870" cy="680" r="7"/>
    </g>
    <g stroke="#fff" stroke-width="4">
      <circle cx="250" cy="671" r="55" fill="#c8102e"/>
      <circle cx="255" cy="484" r="55" fill="#1e3a8a"/>
      <circle cx="389" cy="329" r="55" fill="#3a4a6b"/>
      <circle cx="600" cy="247" r="55" fill="#1f44a8"/>
      <circle cx="810" cy="311" r="55" fill="#243f8c"/>
      <circle cx="923" cy="489" r="55" fill="#d8261c"/>
      <circle cx="936" cy="671" r="55" fill="#b3261e"/>
    </g>
    <circle cx="600" cy="560" r="16" fill="#1f3466"/>
    <text x="600" y="620" text-anchor="middle" font-family="Raleway, Arial, sans-serif" font-weight="800" font-size="56" fill="#1d2233">BRIGHT CAMPUS</text>
  </svg>
  <div role="img" aria-label="Country flag badges for each study destination" class="abs" style="left:0;top:0;width:1px;height:1px"></div>
  <p class="dest-label" style="left:125px;top:578px">Study in<br><b>Malaysia</b></p>
  <p class="dest-label" style="left:190px;top:383px">Study in<br><b>Australia</b></p>
  <p class="dest-label" style="left:305px;top:224px">Study<br><b>English Language</b></p>
  <p class="dest-label" style="left:657px;top:176px;text-align:left">Study in<br><b>Europe</b></p>
  <p class="dest-label" style="left:838px;top:225px;text-align:left">Study in<br><b>New Zealand</b></p>
  <p class="dest-label" style="left:922px;top:402px">Study in<br><b>China</b></p>
  <p class="dest-label" style="left:1000px;top:576px;text-align:left">Study in<br><b>Germany</b></p>
</section>

<!-- application -->
<section class="apply">
  <div class="apply-photo" role="img" aria-label="Photo of a smiling graduate in cap and gown, blue duotone"></div>
  <h2>Make an Application</h2>
  <div class="field" style="top:145px">Name <em>*</em></div>
  <div class="field" style="top:198px">Email <em>*</em></div>
  <div class="field" style="top:251px">Phone</div>
  <div class="apply-btn">Apply Now</div>
</section>

<!-- why -->
<h2 class="sec-title" style="top:2518px">WHO <b>BRIGHT CAMPUS?</b></h2>
<div class="cards">
  <div class="card">
    <div class="icon"><svg viewBox="0 0 24 24"><circle cx="12" cy="8" r="4" fill="#1f3466"/><path d="M4 21c0-4.4 3.6-7 8-7s8 2.6 8 7z" fill="#1f3466"/></svg></div>
    <h4>Experienced Counselling &amp; advice based on you</h4>
    <p>Experienced counselors available to help you identify the best education plan for you!</p>
  </div>
  <div class="card">
    <div class="icon"><svg viewBox="0 0 24 24"><path d="M3 5h7a2 2 0 0 1 2 2v13a2 2 0 0 0-2-2H3zM21 5h-7a2 2 0 0 0-2 2v13a2 2 0 0 1 2-2h7z" fill="#1f3466"/></svg></div>
    <h4>Partnerships with a global network of universities &amp; educational institutions</h4>
    <p>We officially collaborate with over 300 domestic and international accredited educational institutions to ensure you get the best quality.</p>
  </div>
  <div class="card">
    <div class="icon"><svg viewBox="0 0 24 24"><circle cx="12" cy="12" r="10" fill="none" stroke="#1f3466" stroke-width="2"/><path d="M2 12h20M12 2c3 3 3 17 0 20M12 2c-3 3-3 17 0 20" stroke="#1f3466" stroke-width="1.6" fill="none"/></svg></div>
    <h4>Wide Range of Countries</h4>
    <p>From China East to Canada West, going through USA, UK, Europe and more. We can help you decide which country is the most suitable for you based on your circumstances.</p>
  </div>
  <div class="card">
    <div class="icon"><svg viewBox="0 0 24 24"><rect x="5" y="3" width="14" height="18" rx="2" fill="#1f3466"/><path d="M8 9h8M8 13h8M8 17h5" stroke="#fff" stroke-width="1.6"/></svg></div>
    <h4>Registration and Accreditation</h4>
    <p>Registered with the National Board of Higher Learning, UAE. We are also members of multiple quality assurance and global educational associations.</p>
  </div>
</div>
<div class="read-more">Read More</div>

<!-- partners -->
<section class="partners">
  <h2 class="sec-title" style="top:78px">OUR <b>PARTNERS</b></h2>
  <div class="badge" style="left:215px;top:212px;width:100px;height:100px;border-radius:50%;background:#c9b98a"></div>
  <div class="badge" style="left:395px;top:208px;width:88px;height:108px;background:#b89a5a"></div>
  <div class="badge" style="left:640px;top:200px;width:124px;height:124px;border-radius:10px;background:#2f6fb3"></div>
  <div class="badge" style="left:855px;top:237px;width:150px;height:50px;background:#2a57c8"></div>
</section>

<!-- newsletter -->
<section class="newsletter">
  <div class="nl-icon"><svg width="20" height="16" viewBox="0 0 20 16"><rect x="1" y="1" width="18" height="14" rx="2" fill="#555"/><path d="M2 2l8 6 8-6" stroke="#d9d9d9" stroke-width="1.5" fill="none"/></svg></div>
  <h5>News letter Signup</h5>
  <svg class="chev" width="22" height="36" viewBox="0 0 22 36"><path d="M4 2l14 16L4 34" stroke="#fff" stroke-width="3" fill="none"/></svg>
  <div class="nl-input">Enter Your Email</div>
  <div class="nl-btn">SUBSCRIBE</div>
</section>

<!-- footer -->
<footer class="footer">
  <div class="footer-brand">BRIGHT<br>CAMPUS</div>
  <div class="footer-social"><i></i><i></i><i></i><i></i><i></i></div>
  <h6 style="left:403px">CONTACT US</h6>
  <address>
    Al Noor Sports Park<br>
    Tower B, Suite 31<br>
    3rd Floor, PO Box 5550<br>
    Phone: +971 2 555 01 10<br>
    Mobile: 971 52 555 0122<br>
    +971 505550133<br>
    +971 50 555 0144<br>
    Email: info@brightcampuslink.ae
  </address>
  <h6 style="left:693px">GET IN TOUCH</h6>
  <div class="gi" style="left:693px;top:94px;width:135px">Name</div>
  <div class="gi" style="left:835px;top:94px;width:135px">Phone</div>
  <div class="gi" style="left:977px;top:94px;width:135px">Email</div>
  <div class="gi desc" style="left:693px;top:140px;width:419px">Description</div>
  <div class="submit" style="top:230px">SUBMIT</div>
</footer>
<div class="copyright">© 2018 brightcampus All Right Reserved</div>

</body>
</html>
```